Mortgage Loan officer needs clean/modern business card design

Looking for a clean, modern 2-sided business card design. We like the earth tones used in our logo and website http://vukarhome-lending.example . Would also like to incorporate: 1) Something special to make our card stand out - a pop of color or embossed logo, for instance and 2) please include "Mortgage Loans" "Reverse Mortgages" "Private Money Loans" on back of card with the logo.

Front: Needs to include agent/company license info - see website. Agent name: Niall Hargrove

Here are fonts and colors used for our logo:
Font: Avenir Next
Colors:
#2c3539 - Dark Gray
#576870 - Light Gray
#ffffff - Background White

Target Market(s)

Prospects and current clients. Will also be distributing to people in professional network (attorneys and CPAs)

Industry/Entity Type

Business

Contact Information for Business Card

Include agent name, contact info, website on front, licensing info for agent an company. Logo and services offered on back

Font styles to use
Other font styles liked:
• Avenir Next

Requirements
Must have
• See project description
Should not have
• Nothing cheesy

```html
<!DOCTYPE html>
<html lang="en">
<head>
<meta charset="utf-8">
<title>Niall Hargrove – Business Card</title>
<link href="https://fonts.googleapis.com/css2?family=Nunito+Sans:wght@400;600&display=swap" rel="stylesheet">
<style>
  :root {
    --page-bg: #e7e5e2;
    --panel-dark: #2c3539;
    --panel-deep: #14191c;
    --panel-mid: #576870;
    --frost: #dcdedd;
    --frost-light: #f1f1ef;
    --ring: #ffffff;
    --text-light: #d6dadc;
    --text-soft: #b9c0c3;
    --text-warm: #c9a99a;
    --logo-ink: #2c3539;
  }
  * { margin: 0; padding: 0; box-sizing: border-box; }
  html, body { width: 1200px; height: 969px; overflow: hidden; }
  body {
    background: var(--page-bg);
    font-family: "Nunito Sans", "Avenir Next", sans-serif;
    position: relative;
  }
  .business-card {
    position: absolute;
    left: 100px; top: 201px;
    width: 1000px; height: 567px;
    border-radius: 26px;
    overflow: hidden;
    box-shadow: 0 18px 40px rgba(0,0,0,0.18);
  }
  .card-art { position: absolute; inset: 0; }
  .agent-info {
    position: absolute;
    left: 48px; top: 52px;
    width: 400px;
    color: var(--text-light);
  }
  .agent-name {
    font-size: 38px; font-weight: 600;
    letter-spacing: 1px; color: var(--text-soft);
    line-height: 1.1;
    white-space: nowrap;
  }
  .agent-title { font-size: 28px; font-weight: 400; margin-top: 6px; line-height: 1.1; }
  .divider {
    border-top: 2px dotted rgba(214,218,220,0.55);
    width: 370px; margin: 22px 0 18px;
  }
  .contact-list { list-style: none; }
  .contact-list li {
    display: flex; align-items: center;
    font-size: 23px; height: 38px;
    white-space: nowrap;
  }
  .contact-list svg { width: 22px; height: 22px; margin-right: 16px; fill: var(--text-light); flex: none; }
  .license { font-size: 23px; line-height: 36px; white-space: nowrap; }
  .address { font-size: 23px; color: var(--text-warm); line-height: 36px; margin-top: 2px; white-space: nowrap; }
  .brand-mark {
    position: absolute;
    left: 542px; top: 77px;
    width: 412px; height: 412px;
    display: flex; align-items: center; justify-content: center;
    text-align: center;
  }
  .brand-name {
    font-size: 46px; font-weight: 400;
    color: var(--logo-ink);
    line-height: 1.15;
  }
</style>
</head>
<body>
  <div class="business-card">
    <svg class="card-art" viewBox="0 0 1000 567" xmlns="http://www.w3.org/2000/svg" aria-hidden="true">
      <defs>
        <linearGradient id="darkPanel" x1="0" y1="0" x2="1" y2="0.3">
          <stop offset="0" stop-color="#2c3539"/>
          <stop offset="0.55" stop-color="#1b2124"/>
          <stop offset="1" stop-color="#0f1315"/>
        </linearGradient>
        <radialGradient id="frostPanel" cx="0.5" cy="0.45" r="0.6">
          <stop offset="0" stop-color="#f1f1ef"/>
          <stop offset="1" stop-color="#cfd2d1"/>
        </radialGradient>
      </defs>
      <rect width="1000" height="567" fill="url(#frostPanel)"/>
      <path d="M0 0 H748 V-6 A289 289 0 0 0 459 283 A289 289 0 0 0 748 572 V567 H0 Z" fill="url(#darkPanel)"/>
      <rect x="740" y="0" width="260" height="567" fill="url(#frostPanel)"/>
      <circle cx="748" cy="283" r="289" fill="url(#frostPanel)"/>
      <circle cx="748" cy="283" r="298" fill="none" stroke="var(--ring)" stroke-width="2" opacity="0.8"/>
      <circle cx="748" cy="283" r="289" fill="none" stroke="var(--ring)" stroke-width="3"/>
      <circle cx="748" cy="283" r="206" fill="none" stroke="var(--logo-ink)" stroke-width="2"/>
    </svg>

    <div class="agent-info">
      <h1 class="agent-name">NIALL HARGROVE</h1>
      <p class="agent-title">CEO/Founder</p>
      <div class="divider"></div>
      <ul class="contact-list">
        <li><svg viewBox="0 0 24 24"><path d="M6.6 10.8a15 15 0 0 0 6.6 6.6l2.2-2.2a1 1 0 0 1 1-.25 11.4 11.4 0 0 0 3.6.57 1 1 0 0 1 1 1V20a1 1 0 0 1-1 1A17 17 0 0 1 3 4a1 1 0 0 1 1-1h3.5a1 1 0 0 1 1 1c0 1.25.2 2.45.57 3.57a1 1 0 0 1-.25 1z"/></svg>415-555-0142 x118</li>
        <li><svg viewBox="0 0 24 24"><path d="M6.6 10.8a15 15 0 0 0 6.6 6.6l2.2-2.2a1 1 0 0 1 1-.25 11.4 11.4 0 0 0 3.6.57 1 1 0 0 1 1 1V20a1 1 0 0 1-1 1A17 17 0 0 1 3 4a1 1 0 0 1 1-1h3.5a1 1 0 0 1 1 1c0 1.25.2 2.45.57 3.57a1 1 0 0 1-.25 1z"/></svg>415-555-0187</li>
        <li><svg viewBox="0 0 24 24"><path d="M7 3h10v5H7zM4 9h16a2 2 0 0 1 2 2v6h-4v4H6v-4H2v-6a2 2 0 0 1 2-2zm4 7v3h8v-3z"/></svg>415-555-0163</li>
        <li><svg viewBox="0 0 24 24"><path d="M2 5h20v14H2zm2 2v.5l8 5 8-5V7zm0 2.8V17h16V9.8l-8 5z"/></svg>vukarhome-lending.example</li>
        <li><svg viewBox="0 0 24 24"><path d="M12 2a10 10 0 1 0 0 20 10 10 0 0 0 0-20zm-1 17.9A8 8 0 0 1 4.2 10.8L9 15.5v1a2 2 0 0 0 2 2zm6.9-2.5A2 2 0 0 0 16 16h-1v-3a1 1 0 0 0-1-1H8v-2h2a1 1 0 0 0 1-1V7h2a2 2 0 0 0 2-2v-.4a8 8 0 0 1 2.9 12.8z"/></svg>www.vukarhome-lending.example</li>
      </ul>
      <div class="divider"></div>
      <p class="license">Lic No :NMLS:512907</p>
      <p class="address">2480 Harbor Lane<br>Suite 210, Fairview, CA 90210</p>
    </div>

    <div class="brand-mark">
      <p class="brand-name">The Hargrove<br>Group</p>
    </div>
  </div>
</body>
</html>
```